I need business cards for a company that will be an umbrella for many retail stores. I need them to be sleek and modern. I would like some white and black in the background of the card as these are the office colours the logo is attached.
Target Market(s)
worldwide
Industry/Entity Type
Business
Requirements
Must have
- traditional business card shape
Should not have
- too many colours
no swirly text

```html
<!DOCTYPE html>
<html lang="en">
<head>
<meta charset="utf-8">
<title>Orvena General Trading – Business Card</title>
<link rel="stylesheet" href="https://fonts.googleapis.com/css2?family=Open+Sans:wght@400;700&family=Questrial&display=swap">
<style>
  :root {
    --page-bg: #e9e7e4;
    --card-white: #ffffff;
    --band-black: #060606;
    --band-lift: #2a2a2a;
    --accent-blue: #1b8ad6;
    --brand-blue: #1d3f86;
    --brand-pale: #c9d4ea;
    --text-white: #ffffff;
    --rule-grey: #6d6d6d;
  }
  * { box-sizing: border-box; margin: 0; padding: 0; }
  html, body { width: 1200px; height: 900px; overflow: hidden; }
  body { background: var(--page-bg); position: relative; }

  .card {
    position: absolute;
    width: 737px;
    height: 424px;
    overflow: hidden;
    box-shadow: 0 6px 14px rgba(0, 0, 0, 0.28);
  }

  .band-texture {
    position: absolute;
    inset: 0;
    background: linear-gradient(100deg, var(--band-black) 0%, #101010 50%, var(--band-black) 100%);
  }

  .brand {
    display: flex;
    align-items: center;
    font-family: "Questrial", sans-serif;
    font-variant: small-caps;
    letter-spacing: 0.04em;
  }
  .brand-dot { flex: none; }
  .brand-name { line-height: 1.1; }

  /* Front card */
  .card-front { left: 400px; top: 18px; background: var(--band-black); }
  .card-front .brand-strip {
    height: 149px;
    background: linear-gradient(180deg, var(--card-white) 0%, #f4f4f4 70%, #e2e2e2 100%);
    display: flex;
    align-items: center;
    padding-left: 120px;
    padding-top: 18px;
  }
  .card-front .brand { gap: 22px; }
  .card-front .brand-dot { width: 50px; height: 50px; }
  .card-front .brand-name { font-size: 24px; color: var(--brand-blue); }

  .card-front .info-band {
    position: relative;
    height: 275px;
  }
  .info-content {
    position: relative;
    text-align: center;
    color: var(--text-white);
    padding-top: 28px;
    padding-right: 26px;
  }
  .person-name {
    font-family: "Open Sans", sans-serif;
    font-weight: 700;
    font-size: 50px;
    line-height: 1.1;
  }
  .name-rule {
    width: 364px;
    height: 1px;
    margin: 4px auto 6px;
    background: linear-gradient(90deg, transparent, var(--rule-grey) 20%, var(--rule-grey) 80%, transparent);
  }
  .person-role {
    font-family: "Open Sans", sans-serif;
    font-weight: 700;
    font-size: 14px;
    letter-spacing: 0.04em;
    color: var(--accent-blue);
    margin-bottom: 22px;
  }
  .contact-list { list-style: none; font-family: "Questrial", sans-serif; font-size: 19px; }
  .contact-list li { line-height: 34px; }
  .contact-label { color: var(--accent-blue); }

  /* Back card */
  .card-back {
    left: 48px;
    top: 458px;
    background: linear-gradient(180deg, #d2d2d2 0%, #ececec 45%, var(--card-white) 100%);
  }
  .card-back .logo-band {
    position: absolute;
    left: 0;
    top: 122px;
    width: 100%;
    height: 201px;
    box-shadow: 0 10px 14px rgba(0, 0, 0, 0.25);
  }
  .card-back .band-texture {
    background:
      radial-gradient(ellipse 300px 170px at 330px 100px, var(--band-lift), transparent 75%),
      var(--band-black);
  }
  .card-back .brand {
    position: absolute;
    left: 215px;
    top: 50%;
    transform: translateY(-50%);
    gap: 22px;
  }
  .card-back .brand-dot { width: 62px; height: 62px; }
  .card-back .brand-name { font-size: 36px; color: var(--brand-pale); }

  .website {
    position: absolute;
    left: 0;
    top: 334px;
    width: 100%;
    text-align: center;
    padding-left: 92px;
    font-family: "Open Sans", sans-serif;
    font-weight: 400;
    font-size: 17px;
    color: var(--brand-blue);
    letter-spacing: 0.02em;
  }
</style>
</head>
<body>

  <section class="card card-front" aria-label="Business card front">
    <header class="brand-strip">
      <div class="brand">
        <svg class="brand-dot" viewBox="0 0 50 50" aria-hidden="true">
          <circle cx="25" cy="25" r="25" fill="var(--brand-blue)"/>
        </svg>
        <span class="brand-name">Orvena<br>General Trading</span>
      </div>
    </header>
    <div class="info-band">
      <div class="band-texture" role="img" aria-label="Black band with diagonal pinstripe texture"></div>
      <div class="info-content">
        <h1 class="person-name">Name J. Name</h1>
        <div class="name-rule"></div>
        <p class="person-role">FOUNDER AND CEO</p>
        <ul class="contact-list">
          <li><span class="contact-label">OFFICE:</span> 90047812(5)</li>
          <li><span class="contact-label">MOBILE:</span> 30258174(13)</li>
          <li><span class="contact-label">EMAIL:</span> NameJN@orvena.com</li>
        </ul>
      </div>
    </div>
  </section>

  <section class="card card-back" aria-label="Business card back">
    <div class="logo-band">
      <div class="band-texture" role="img" aria-label="Black band with diagonal pinstripe texture and soft light glow"></div>
      <div class="brand">
        <svg class="brand-dot" viewBox="0 0 62 62" aria-hidden="true">
          <circle cx="31" cy="31" r="31" fill="var(--brand-pale)"/>
        </svg>
        <span class="brand-name">Orvena<br>General Trading</span>
      </div>
    </div>
    <p class="website">www.official website.com</p>
  </section>

</body>
</html>
```